14 and Wrens Bar and Grill Menu 2016

Our property is currently going through a renovation to modernize the look and feel of the unit. 14 and Wrens is a restaurant attached to a Dellaway branded hotel in WI and we are making changes as well to provide a gathering place for both guests inside and outside of the hotel.
We need a new menu layout to help attract the local market for our restaurant. We are going for hip and trendy, easy to read, with a layout that is different from the normal fold that is seen everywhere. I have included the logo
Attached is a menu we really like to help give an idea of our style

Target Market(s)

25-45yr old

Industry/Entity Type

American Restaurant

Font styles to use
Other font styles liked:
• Isabel Bold

Colors
1b1b1b
ec1f27
ffffff
d5d5d5

Requirements
Must have
• Must have multiple pages, bold fonts, and easy to change out pages if necessary
• photo on the front for a fun bar and grill type feel
• Menu included with page breaks
Nice to have
• bold headers for each category
• fun tag lines for each category
Should not have
• many pictures aside from the front and back pages of the menu

```html
<!DOCTYPE html>
<html lang="en">
<head>
<meta charset="utf-8">
<title>14 and Wrens Bar and Grill – Appetizers</title>
<link rel="stylesheet" href="https://fonts.googleapis.com/css2?family=Alfa+Slab+One&family=Bebas+Neue&family=Lobster&family=Montserrat:wght@600;700;800&family=Rye&display=swap">
<style>
  :root {
    --ink: #1b1b1b;
    --ink-deep: #0e0e0e;
    --ink-lift: #2a2a2a;
    --chalk: #ffffff;
    --chalk-soft: #d5d5d5;
  }
  * { box-sizing: border-box; margin: 0; padding: 0; }
  html, body { width: 848px; height: 1200px; overflow: hidden; background: var(--ink); }
  .menu-page {
    position: relative;
    width: 848px;
    height: 1200px;
    overflow: hidden;
    color: var(--chalk);
    background: radial-gradient(ellipse at 45% 35%, var(--ink-lift) 0%, var(--ink) 55%, var(--ink-deep) 100%);
    font-family: "Montserrat", sans-serif;
  }
  .brand {
    position: absolute;
    left: 274px; top: 40px;
    width: 300px; height: 116px;
    display: flex; align-items: center; justify-content: center;
  }
  .brand-name {
    font-family: "Montserrat", sans-serif;
    font-weight: 700;
    font-size: 20px;
    line-height: 1.3;
    color: var(--chalk);
    text-align: center;
    text-transform: uppercase;
    letter-spacing: 3px;
  }
  .section-title {
    position: absolute;
    left: 0; top: 182px; width: 848px;
    text-align: center;
    font-weight: 700;
    font-size: 27px;
    letter-spacing: 11px;
  }
  .dish { position: absolute; text-align: center; white-space: nowrap; }
  .dish-col-left { left: 34px; width: 352px; }
  .dish-col-right { left: 420px; width: 390px; }
  .dish-slab { font-family: "Alfa Slab One", serif; line-height: 1.05; display: block; }
  .dish-condensed { font-family: "Bebas Neue", sans-serif; line-height: 0.95; display: block; text-transform: uppercase; }
  .dish-script { font-family: "Lobster", cursive; line-height: 1; display: block; }
  .dish-caps { font-family: "Rye", serif; line-height: 1.1; display: block; letter-spacing: 3px; }
  .dish-spaced { font-family: "Montserrat", sans-serif; font-weight: 800; line-height: 1.1; display: block; }
  .dish-price { font-size: 0.6em; }
  .dish-rule { display: block; height: 1px; margin: 6px auto; background: var(--chalk-soft); opacity: .6; }
  .dish-desc {
    display: block;
    margin-top: 12px;
    font-weight: 700;
    font-size: 9.5px;
    line-height: 15px;
    letter-spacing: .4px;
    text-transform: uppercase;
    white-space: normal;
  }
  .dish-options { font-size: 12px; letter-spacing: .6px; }
  .service-note {
    position: absolute;
    left: 0; top: 1164px; width: 848px;
    text-align: center;
    font-weight: 600;
    font-size: 9.5px;
    letter-spacing: .8px;
    text-transform: uppercase;
  }
</style>
</head>
<body>
<main class="menu-page">
  <header class="brand">
    <span class="brand-name">14 and Wrens<br>Bar and Grill</span>
  </header>

  <h1 class="section-title">APPETIZERS</h1>

  <section class="dish dish-col-left" style="top:262px">
    <span class="dish-slab" style="font-size:32px;letter-spacing:3px">BRUSCHETTA<span class="dish-price">9</span></span>
    <span class="dish-rule" style="width:78%"></span>
    <span class="dish-desc" style="margin-top:8px">Tomato, basil, garlic, olive oil, Parmesan cheese,<br>Parmesan crostinis | w/ shrimp 14</span>
  </section>

  <section class="dish dish-col-left" style="top:408px">
    <span class="dish-condensed" style="font-size:58px;letter-spacing:2px">Spinach &amp;</span>
    <span class="dish-condensed" style="font-size:58px;letter-spacing:1px">Artichoke Dip <span class="dish-price">9</span></span>
    <span class="dish-desc" style="margin-top:18px">Spinach, artichoke, Parmesan, garlic,<br>house-made, crispy tortilla chips</span>
  </section>

  <section class="dish dish-col-left" style="top:628px">
    <span class="dish-script" style="font-size:46px">Crunchy</span>
    <span class="dish-slab" style="font-size:52px;letter-spacing:1px">CHICKEN</span>
    <span class="dish-spaced" style="font-size:28px;letter-spacing:6px;margin-top:2px">FINGERS 10</span>
    <span class="dish-rule" style="width:78%"></span>
    <span class="dish-desc" style="margin-top:10px">Hand breaded, deep fried</span>
  </section>

  <section class="dish dish-col-left" style="top:892px">
    <span class="dish-script" style="font-size:42px">Smoked</span>
    <span class="dish-slab" style="font-size:46px;letter-spacing:3px">WINGS <span class="dish-price">11</span></span>
    <span class="dish-rule" style="width:78%"></span>
    <span class="dish-desc" style="margin-top:8px">Buffalo, barbecue, Szechwan or en fuego<br><span class="dish-options">Boneless 10 | Traditional 11</span></span>
  </section>

  <section class="dish dish-col-right" style="top:312px">
    <span class="dish-slab" style="font-size:60px;letter-spacing:1px">CHICKEN</span>
    <span class="dish-spaced" style="font-size:28px;letter-spacing:7px;margin-top:2px">NACHOS 10</span>
    <span class="dish-rule" style="width:66%"></span>
    <span class="dish-desc" style="margin-top:10px">Grilled chicken, queso, black beans, jalapeño,<br>cilantro, pico de gallo, guacamole, sour cream,<br>tortilla chips</span>
  </section>

  <section class="dish dish-col-right" style="top:516px">
    <span class="dish-script" style="font-size:46px">Crunchy</span>
    <span class="dish-slab" style="font-size:38px;text-transform:lowercase">vegetables</span>
    <span class="dish-caps" style="font-size:22px;margin-top:2px">FLATBREADS 11</span>
    <span class="dish-rule" style="width:70%"></span>
    <span class="dish-desc" style="margin-top:6px">Fresh spinach &amp; artichoke sauce, tomato, mushrooms, basil,<br>balsamic onions, mozzarella and provolone cheese blend</span>
  </section>

  <section class="dish dish-col-right" style="top:736px">
    <span class="dish-slab" style="font-size:40px;letter-spacing:2px">BUFFALO</span>
    <span class="dish-slab" style="font-size:58px;letter-spacing:1px">CHICKEN</span>
    <span class="dish-caps" style="font-size:24px;margin-top:2px">FLATBREADS 11</span>
    <span class="dish-rule" style="width:70%"></span>
    <span class="dish-desc" style="margin-top:8px">Grilled chicken, green onion, blue cheese crumbles,<br>buffalo sauce, smoked onion ranch, mozzarella and<br>provolone cheese blend</span>
  </section>

  <p class="service-note">An 18% service charge will be added to all purchases for parties of 8 or more.</p>
</main>
</body>
</html>
```